The name of the company is Torvend Holdings, LLC. I would like a business card with a logo.

On the top left, I would like a logo design of a crown and I would like Torvend over the top of the crown while Holdings on the bottom. Please see attached files as an example of crown and positioning of Torvend Holdings. Then I would like the letters TH in the middle(see picture).

Colors

Designer to choose colors to be used in the design.

```html
<!DOCTYPE html>
<html lang="en">
<head>
<meta charset="utf-8">
<title>Torvend Holdings, LLC — Business Card</title>
<link href="https://fonts.googleapis.com/css2?family=Lato:wght@400;700&display=swap" rel="stylesheet">
<style>
  :root {
    --stage: #e6e1d8;
    --card: #000000;
    --gold: #e8cf9a;
    --silver: #c4c4c4;
    --crown-red: #7a1616;
    --crown-gold: #c99a4a;
    --crown-green: #2f5a48;
  }
  * { margin: 0; padding: 0; box-sizing: border-box; }
  html, body {
    width: 1200px; height: 1023px; overflow: hidden;
    background: var(--stage);
    font-family: "Lato", sans-serif;
  }
  .canvas { position: relative; width: 1200px; height: 1023px; }
  .card {
    position: absolute; left: 248px; width: 681px; height: 397px;
    background: var(--card);
    box-shadow: 0 4px 14px rgba(0,0,0,0.25);
  }
  .card--front { top: 87px; }
  .card--back { top: 541px; }

  .crown-emblem {
    position: absolute;
    border-radius: 40% 40% 10% 10%;
    background: linear-gradient(180deg, var(--crown-green) 0%, var(--crown-green) 30%, var(--crown-red) 45%, var(--crown-gold) 100%);
  }
  .card--front .crown-emblem { left: 91px; top: 30px; width: 120px; height: 171px; }
  .card--back .crown-emblem { left: 253px; top: 38px; width: 178px; height: 258px; }

  .company-name { color: var(--gold); font-weight: 400; white-space: nowrap; }
  .card--front .company-name { position: absolute; left: 25px; top: 210px; font-size: 24px; }
  .card--back .company-name {
    position: absolute; left: 0; right: 0; top: 310px;
    text-align: center; font-size: 37px;
  }

  .person { position: absolute; right: 33px; top: 48px; text-align: right; }
  .person__name { color: var(--gold); font-size: 32px; font-weight: 700; }
  .person__title { color: var(--silver); font-size: 18px; margin-top: 6px; }

  .address {
    position: absolute; left: 25px; top: 258px;
    color: var(--silver); font-size: 15.5px; line-height: 20px; font-style: normal;
  }
  .contact { position: absolute; left: 25px; color: var(--silver); font-size: 15.5px; display: flex; align-items: center; }
  .contact--phone { top: 320px; }
  .contact--email { top: 348px; }
  .contact svg { width: 14px; height: 14px; margin-right: 11px; fill: var(--silver); }
</style>
</head>
<body>
<main class="canvas">
  <section class="card card--front">
    <div class="crown-emblem" role="img" aria-label="Jewelled crown emblem with feather plume"></div>
    <div class="company-name">Torvend Holdings, LLC</div>
    <div class="person">
      <div class="person__name">Navid Rostani, MBA</div>
      <div class="person__title">Founder / CEO</div>
    </div>
    <address class="address">418 Alder Crest Road, Suite 200<br>Fairmont Ridge, CA. 90311</address>
    <div class="contact contact--phone">
      <svg viewBox="0 0 24 24" aria-hidden="true"><path d="M6.6 10.8a15.1 15.1 0 0 0 6.6 6.6l2.2-2.2a1 1 0 0 1 1-.25 11.4 11.4 0 0 0 3.6.57 1 1 0 0 1 1 1V20a1 1 0 0 1-1 1A17 17 0 0 1 3 4a1 1 0 0 1 1-1h3.5a1 1 0 0 1 1 1c0 1.25.2 2.45.57 3.6a1 1 0 0 1-.25 1z"/></svg>
      <span>(310) 555-0148</span>
    </div>
    <div class="contact contact--email">
      <svg viewBox="0 0 24 24" aria-hidden="true"><path d="M2 5h20v14H2z M3.5 6.5 12 13l8.5-6.5" fill="none" stroke="#c4c4c4" stroke-width="2"/></svg>
      <span>mTorvend.Holdings@mailbox.com</span>
    </div>
  </section>

  <section class="card card--back">
    <div class="crown-emblem" role="img" aria-label="Jewelled crown emblem with feather plume"></div>
    <div class="company-name">Torvend Holdings, LLC</div>
  </section>
</main>
</body>
</html>
```